Lena Corvell Business Card

I need a business card that reflects my current website: itslenacorvell.example and screenshot attached. If we keep the color scheme of the site and sample card below that would be ideal. The business card should include the information on the attached sample cards.

Industry/Entity Type

Business

```html
<!DOCTYPE html>
<html lang="en">
<head>
<meta charset="utf-8">
<title>Lena Corvell Business Card</title>
<link rel="stylesheet" href="https://fonts.googleapis.com/css2?family=Josefin+Sans:ital,wght@0,300;1,300&display=swap">
<style>
  :root {
    --paper: #ffffff;
    --card-mint: #61fe9e;
    --ink-light: #ffffff;
    --chip-lime: #5fd91a;
    --chip-red: #ff4230;
    --chip-pink: #ff52f5;
    --chip-plum: #2e1b2a;
    --chip-aqua: #52ffb5;
    --chip-yellow: #f8ea1c;
    --signature-tone: #1c1c1c;
  }
  html, body {
    margin: 0;
    padding: 0;
    width: 1200px;
    height: 943px;
    overflow: hidden;
    background: var(--paper);
  }
  .canvas {
    position: relative;
    width: 1200px;
    height: 943px;
    font-family: "Josefin Sans", sans-serif;
    font-weight: 300;
    color: var(--ink-light);
  }
  .chip-row {
    position: absolute;
    left: 85px;
    top: 138px;
  }
  .card {
    position: absolute;
    left: 85px;
    top: 176px;
    width: 1030px;
    height: 591px;
    background: var(--card-mint);
  }
  .card-text {
    position: absolute;
    left: 42px;
    margin: 0;
    white-space: nowrap;
    line-height: 1;
    font-weight: 300;
  }
  .name { top: 62px; font-size: 44px; letter-spacing: 1px; }
  .roles { top: 150px; font-size: 35px; font-style: italic; letter-spacing: -0.5px; }
  .email { top: 228px; font-size: 34px; }
  .phone { top: 262px; font-size: 34px; }
  .social {
    position: absolute;
    left: 42px;
    top: 336px;
    display: flex;
    align-items: center;
    gap: 12px;
    font-size: 32px;
  }
  .social-mark {
    width: 34px;
    height: 34px;
    background: var(--ink-light);
    border-radius: 4px;
  }
  .website { top: 412px; font-size: 33px; letter-spacing: 0.5px; }
  .signature {
    position: absolute;
    left: 339px;
    top: 354px;
    width: 646px;
    height: 216px;
  }
</style>
</head>
<body>
<div class="canvas">
  <svg class="chip-row" width="1030" height="38" viewBox="0 0 1030 38" aria-hidden="true">
    <rect x="0" y="0" width="45" height="38" fill="var(--chip-lime)"/>
    <rect x="89.5" y="0" width="45" height="38" fill="var(--chip-red)"/>
    <rect x="179" y="0" width="45" height="38" fill="var(--chip-pink)"/>
    <rect x="268.5" y="0" width="45" height="38" fill="var(--chip-plum)"/>
    <rect x="358" y="0" width="45" height="38" fill="var(--chip-aqua)"/>
    <rect x="447.5" y="0" width="45" height="38" fill="var(--chip-yellow)"/>
    <rect x="537" y="0" width="45" height="38" fill="var(--chip-lime)"/>
    <rect x="626.5" y="0" width="45" height="38" fill="var(--chip-red)"/>
    <rect x="716" y="0" width="45" height="38" fill="var(--chip-pink)"/>
    <rect x="805.5" y="0" width="45" height="38" fill="var(--chip-plum)"/>
    <rect x="895" y="0" width="45" height="38" fill="var(--chip-aqua)"/>
    <rect x="985" y="0" width="45" height="38" fill="var(--chip-yellow)"/>
  </svg>

  <section class="card">
    <h1 class="card-text name">Lena Corvell</h1>
    <p class="card-text roles">Brand Curator | Digital Storyteller | Social Entrpreneur</p>
    <p class="card-text email">me@lenacorvell.example</p>
    <p class="card-text phone">555.014.2290</p>
    <div class="social">
      <span class="social-mark"></span>
      <span class="social-handle">@itslenacorvell</span>
    </div>
    <p class="card-text website">www.itslenacorvell.example</p>
    <svg class="signature" viewBox="0 0 646 216" role="img" aria-label="Hand-lettered signature reading 'its Lena Corvell' in black brush script">
      <path d="M140 0 H646 V216 H0 V116 H140 Z" fill="var(--signature-tone)" opacity="0.85"/>
    </svg>
  </section>
</div>
</body>
</html>
```